手延うどん(乾麺)のパッケージデザイン(製品袋)を依頼させて頂きます。和紙系か和紙雲竜系の袋を考えていますので高級感のあるデザインを希望します。ターゲット層は40-60代の価格ではなく美味しさを求めているお客様。何本か並べると綺麗なデザイン。※現在販売しているデザインだと、シンプルすぎるかなと感じています。
サイズ:W50×D27×H25mm
参考に現在のデザイン写真を添付しておきます。
サイズが間違っていました。横50mm、縦270mm、厚み25mmです。
新たな写真を添付致しました。

和のイメージと背景の小麦のデザイン。温故知新も決め手のポイントでした。

今回、たくさんのデザイン案ありがとうございました。ミトリエさんを通してお願いしたのが初めてで、選ぶのに苦労しました・・・。次回もお願いしようと考えているので、機会がございましたら、またよろしくお願い致します。

```html
<!DOCTYPE html>
<html lang="ja">
<head>
<meta charset="utf-8">
<title>上州手延うどん パッケージ</title>
<link rel="stylesheet" href="https://fonts.googleapis.com/css2?family=Yuji+Boku&display=swap">
<style>
  :root {
    --canvas: #ffffff;
    --pack-blue: #3fb6ea;
    --pack-blue-light: #7fd3f6;
    --swirl-yellow: #f3efb0;
    --swirl-white: #ffffff;
    --ink: #151515;
    --seal-red: #d7262b;
  }
  * { margin: 0; padding: 0; box-sizing: border-box; }
  html, body {
    width: 898px;
    height: 1200px;
    overflow: hidden;
    background: var(--canvas);
  }
  .package-row {
    display: flex;
    gap: 12px;
    padding: 10px 15px;
    width: 898px;
    height: 1200px;
  }
  .noodle-pack {
    position: relative;
    flex: 0 0 208px;
    height: 1180px;
    background: var(--pack-blue);
    overflow: hidden;
  }
  .swirl-top {
    position: absolute;
    left: 0; top: 0;
    width: 100%;
    height: 360px;
    background:
      radial-gradient(circle at 70% 18%, rgba(243,239,176,0.55) 0 22%, transparent 40%),
      radial-gradient(circle at 25% 30%, rgba(255,255,255,0.35) 0 18%, transparent 38%),
      linear-gradient(180deg, var(--pack-blue-light), var(--pack-blue));
  }
  .swirl-bottom {
    position: absolute;
    left: 0; bottom: 0;
    width: 100%;
    height: 600px;
    background:
      radial-gradient(circle at 80% 30%, rgba(255,255,255,0.35) 0 20%, transparent 38%),
      radial-gradient(circle at 20% 60%, rgba(255,255,255,0.3) 0 22%, transparent 40%),
      radial-gradient(circle at 70% 88%, rgba(243,239,176,0.4) 0 18%, transparent 36%),
      linear-gradient(180deg, var(--pack-blue), var(--pack-blue-light));
  }
  .product-name {
    position: absolute;
    top: 165px;
    left: 50%;
    transform: translateX(-50%);
    writing-mode: vertical-rl;
    font-family: "Yuji Boku", serif;
    font-size: 112px;
    line-height: 1;
    letter-spacing: -6px;
    color: var(--ink);
    white-space: nowrap;
  }
  .quality-seal {
    position: absolute;
    left: 74px;
    top: 1030px;
    width: 56px;
    height: 56px;
    background: var(--seal-red);
    border: 3px solid var(--swirl-white);
  }
</style>
</head>
<body>
  <main class="package-row">
    <section class="noodle-pack">
      <div class="swirl-top" role="img" aria-label="黄色と白の渦巻き模様"></div>
      <div class="swirl-bottom" role="img" aria-label="白い渦巻き模様"></div>
      <h1 class="product-name">上州手延うどん</h1>
      <div class="quality-seal"></div>
    </section>
    <section class="noodle-pack">
      <div class="swirl-top" role="img" aria-label="黄色と白の渦巻き模様"></div>
      <div class="swirl-bottom" role="img" aria-label="白い渦巻き模様"></div>
      <p class="product-name">上州手延うどん</p>
      <div class="quality-seal"></div>
    </section>
    <section class="noodle-pack">
      <div class="swirl-top" role="img" aria-label="黄色と白の渦巻き模様"></div>
      <div class="swirl-bottom" role="img" aria-label="白い渦巻き模様"></div>
      <p class="product-name">上州手延うどん</p>
      <div class="quality-seal"></div>
    </section>
    <section class="noodle-pack">
      <div class="swirl-top" role="img" aria-label="黄色と白の渦巻き模様"></div>
      <div class="swirl-bottom" role="img" aria-label="白い渦巻き模様"></div>
      <p class="product-name">上州手延うどん</p>
      <div class="quality-seal"></div>
    </section>
  </main>
</body>
</html>
```